Design a Unique and Eye-Catching Necklace Card for Wendaray's New Brightwell Line

Attention all creative minds from around the world! Wendaray, a company known for its free-spirited and bohemian chic vibe, is proud to announce a new design contest. We are inviting you to create a dynamic and unique necklace card for our upcoming Brightwell line.

Our new Brightwell line comprises 12-20 unique necklace combinations. Each necklace features different stones, each with its own healing properties and associated zodiac sign. We are looking for a template that can be easily modified to change the names of the stones, zodiac sign, and the colors to match the specific stones on each necklace.

The card should be 3 x 4,
It should include the names of the stones, the associated zodiac sign (if applicable), a few words about the healing properties of the stones, and a captivating graphic that represents the colors of the stones.

Our goal is to delight our customers with packaging as unique as the necklaces themselves. The necklace should be the focal point, but the text and graphic on the card should also draw the eye.

Please note that our target audience includes mid-priced boutiques across the country and festival-goers in Colorado. Your design should reflect the unique taste and free spirit of our clientele.

We are excited to see your creativity shine in this project. If there are any points that need clarification, please do not hesitate to ask. We look forward to your participation in bringing the Brightwell line to life!
https://www.draftnook.example/board/KQ7mPzR2tLw/edit

https://www.draftnook.example/board/VJ3nHsX8qYb/edit
I want to use the flowing watercolor and have it change with each necklace color.
Use the necklaces below. Incorporate the zodiac symbol as is shown below.

Examples of other cards in our collection

The Little Pebble Pendant: https://www.draftnook.example/board/TB5wGdM4cRu/edit

Other examples of necklace cards I like:

https://www.craftbazaro.example/item/731905284/green-stone-pendant

https://www.craftbazaro.example/item/462918037/birthstone-pendant-green

https://www.craftbazaro.example/item/2907315628/crystal-bead-bracelets

https://www.craftbazaro.example/item/3816402795/dark-stone-guard-pendant

Target Market(s)

Women aged 25-50 with a spiritual, hippy, bohemain, yoga vibe.

Industry/Entity Type

Handmade Jewelry | Wholesale jewelry | Retail Jewelry sales at Festivals

Font styles to use
Script

Colors

Designer to choose colors to be used in the design.

Requirements
Must have
• A template that can be interchangable with the stone colors, names and healing properties.
Nice to have
• Some different ideas about the graphic color patterns on the card.
Should not have
• Any graphic that would cover the middle of the necklace card and keep people from seeing the neckalce

```html
<!DOCTYPE html>
<html lang="en">
<head>
<meta charset="utf-8">
<title>Wendaray Brightwell Necklace Cards</title>
<link href="https://fonts.googleapis.com/css2?family=Poiret+One&family=Josefin+Sans:wght@300;400&display=swap" rel="stylesheet">
<style>
  :root {
    --page: #ffffff;
    --face: #fbfbfa;
    --blue: #3d5fd0;
    --teal: #3aa6a2;
    --plum: #ad4c98;
    --pine: #4b6f64;
  }
  * { box-sizing: border-box; margin: 0; padding: 0; }
  html, body { width: 1200px; height: 403px; overflow: hidden; background: var(--page); }
  .lineup { position: relative; width: 1200px; height: 403px; }
  .card {
    position: absolute; top: 12px; width: 288px; height: 383px; overflow: hidden;
    color: var(--accent);
  }
  .card--aquamarine-kyanite { left: 9px; --accent: var(--blue);
    --wash: radial-gradient(circle at 20% 20%, #bfe6f2 0%, transparent 40%), linear-gradient(150deg, #2f8fb0 0%, #1c5f86 45%, #3db2c4 70%, #0f3e52 100%); }
  .card--chrysocolla-aquamarine { left: 307px; --accent: var(--teal);
    --wash: radial-gradient(circle at 25% 15%, #c9f2e6 0%, transparent 40%), linear-gradient(150deg, #1fa58d 0%, #14786a 45%, #35c3a8 70%, #0c3b35 100%); }
  .card--fluorite { left: 605px; --accent: var(--plum);
    --wash: radial-gradient(circle at 25% 15%, #e6dde8 0%, transparent 40%), linear-gradient(150deg, #5f7f8e 0%, #4b3a5a 45%, #8a7a95 70%, #2a2233 100%); }
  .card--ocean-jasper { left: 903px; --accent: var(--pine);
    --wash: radial-gradient(circle at 30% 15%, #cfe6d9 0%, transparent 40%), linear-gradient(150deg, #3f8a6c 0%, #2f4a40 45%, #5f3a32 75%, #3a1f1c 100%); }

  .card__wash { position: absolute; inset: 0; background: var(--wash); }
  .card__face {
    position: absolute; left: 9px; top: 56px; width: 270px; height: 270px;
    border-radius: 50%; background: var(--face);
  }
  .card__brand {
    position: absolute; top: 76px; width: 100%; text-align: center;
    font-family: "Poiret One", sans-serif; font-size: 11.5px; letter-spacing: 0.3px;
  }
  .card__stones {
    position: absolute; top: 104px; width: 100%; text-align: center;
    font-family: "Poiret One", sans-serif; font-size: 25px; line-height: 25px;
    text-transform: uppercase; letter-spacing: -0.3px;
  }
  .card__necklace { position: absolute; left: 0; top: 148px; width: 288px; height: 95px; }
  .card__sign-art {
    position: absolute; left: 122px; top: 246px; width: 44px; height: 54px;
    border-radius: 22px 22px 8px 8px; background: var(--accent); opacity: 0.22;
  }
  .card__sign {
    position: absolute; top: 313px; width: 100%; text-align: center;
    font-family: "Josefin Sans", sans-serif; font-weight: 400; font-size: 7.5px;
    letter-spacing: 1.6px;
  }
</style>
</head>
<body>
<main class="lineup">

  <section class="card card--aquamarine-kyanite">
    <div class="card__wash" role="img" aria-label="Flowing blue and aqua watercolour marble backdrop"></div>
    <div class="card__face"></div>
    <p class="card__brand">WENDARAY</p>
    <h2 class="card__stones">Aquamarine<br>&amp; Kyanite</h2>
    <svg class="card__necklace" viewBox="0 0 288 95" role="img" aria-label="Necklace of faceted blue kyanite and aquamarine beads">
      <defs><linearGradient id="beads-blue" x1="0" x2="1"><stop offset="0" stop-color="#3a6fe0"/><stop offset="0.5" stop-color="#7fa7e8"/><stop offset="1" stop-color="#3a6fe0"/></linearGradient></defs>
      <path d="M10 12 Q144 80 280 15" fill="none" stroke="#c9ccd2" stroke-width="0.8"/>
      <path d="M40 35 Q144 88 264 38" fill="none" stroke="url(#beads-blue)" stroke-width="14" stroke-linecap="round"/>
    </svg>
    <div class="card__sign-art" role="img" aria-label="Pisces zodiac emblem with two fish"></div>
    <p class="card__sign">PISCES</p>
  </section>

  <section class="card card--chrysocolla-aquamarine">
    <div class="card__wash" role="img" aria-label="Flowing teal and green watercolour marble backdrop"></div>
    <div class="card__face"></div>
    <p class="card__brand">WENDARAY</p>
    <h2 class="card__stones">Chrysocolla<br>&amp; Aquamarine</h2>
    <svg class="card__necklace" viewBox="0 0 288 95" role="img" aria-label="Necklace of chrysocolla and aquamarine beads with silver spacers">
      <defs><linearGradient id="beads-teal" x1="0" x2="1"><stop offset="0" stop-color="#2b7f86"/><stop offset="0.3" stop-color="#5a5048"/><stop offset="0.55" stop-color="#2aa0a8"/><stop offset="0.8" stop-color="#3f5a58"/><stop offset="1" stop-color="#9fd1b8"/></linearGradient></defs>
      <path d="M10 12 Q144 80 280 12" fill="none" stroke="#c9ccd2" stroke-width="0.8"/>
      <path d="M30 30 Q144 88 262 30" fill="none" stroke="url(#beads-teal)" stroke-width="14" stroke-linecap="round"/>
    </svg>
    <div class="card__sign-art" role="img" aria-label="Virgo zodiac emblem"></div>
    <p class="card__sign">VIRGO</p>
  </section>

  <section class="card card--fluorite">
    <div class="card__wash" role="img" aria-label="Flowing violet and slate watercolour marble backdrop"></div>
    <div class="card__face"></div>
    <p class="card__brand">WENDARAY</p>
    <h2 class="card__stones">Fluorite</h2>
    <svg class="card__necklace" viewBox="0 0 288 95" role="img" aria-label="Necklace of faceted clear, purple and green fluorite beads">
      <defs><linearGradient id="beads-plum" x1="0" x2="1"><stop offset="0" stop-color="#e6e2da"/><stop offset="0.3" stop-color="#a98cb8"/><stop offset="0.5" stop-color="#7a2f8f"/><stop offset="0.75" stop-color="#6f8fa0"/><stop offset="1" stop-color="#bfd2cf"/></linearGradient></defs>
      <path d="M8 6 Q144 72 280 4" fill="none" stroke="#c9ccd2" stroke-width="0.8"/>
      <path d="M22 16 Q144 80 270 16" fill="none" stroke="url(#beads-plum)" stroke-width="13" stroke-linecap="round"/>
    </svg>
    <div class="card__sign-art" role="img" aria-label="Pisces zodiac emblem with two fish"></div>
    <p class="card__sign">PISCES</p>
  </section>

  <section class="card card--ocean-jasper">
    <div class="card__wash" role="img" aria-label="Flowing green and russet watercolour marble backdrop"></div>
    <div class="card__face"></div>
    <p class="card__brand">WENDARAY</p>
    <h2 class="card__stones">Ocean<br>Jasper</h2>
    <svg class="card__necklace" viewBox="0 0 288 95" role="img" aria-label="Necklace of ocean jasper beads in green, cream, orange and pink">
      <defs><linearGradient id="beads-pine" x1="0" x2="1"><stop offset="0" stop-color="#3f6e5c"/><stop offset="0.3" stop-color="#2f5f58"/><stop offset="0.5" stop-color="#d8cdb0"/><stop offset="0.75" stop-color="#c8772f"/><stop offset="1" stop-color="#e28a9a"/></linearGradient></defs>
      <path d="M44 -10 Q60 60 144 88 Q230 60 262 -10" fill="none" stroke="url(#beads-pine)" stroke-width="15" stroke-linecap="round"/>
    </svg>
  </section>

</main>
</body>
</html>
```